Income Tax Business Cards - Updates

Need to update these business cards while keeping all the same wording but just update them and make them look nicer and more modern/ on brand with our brand.

Industry/Entity Type

finance

Contact Information for Business Card

we have multiple locations so will just need to easily be able to change the address and phone numbers

Colors

Designer to choose colors to be used in the design.

```html
<!DOCTYPE html>
<html lang="en">
<head>
<meta charset="utf-8">
<title>Ledgerline Financial Group – Business Card</title>
<link href="https://fonts.googleapis.com/css2?family=Lato:wght@400;700;900&display=swap" rel="stylesheet">
<style>
  :root{
    --bg:#8e8e8e;
    --card:#ffffff;
    --green:#0d5130;
    --red:#c01f2a;
    --ink:#333333;
  }
  *{margin:0;padding:0;box-sizing:border-box}
  html,body{width:1200px;height:1200px;overflow:hidden;background:var(--bg);font-family:'Lato',sans-serif}
  .canvas{position:relative;width:1200px;height:1200px}
  .card{position:absolute;left:250px;width:700px;height:400px;border-radius:20px}
  .card--front{top:170px;background:var(--card)}
  .card--back{top:631px;background:var(--green)}

  .brand{position:absolute;display:flex;align-items:center;gap:10px;font-weight:900;line-height:1.05}
  .brand__dot{flex:none;border-radius:50%}
  .card--front .brand{left:66px;top:88px;width:250px;color:var(--green);font-size:30px}
  .card--front .brand__dot{width:22px;height:22px;background:var(--green)}
  .card--back .brand{left:0;right:0;top:100px;justify-content:center;color:#fff;font-size:50px}
  .card--back .brand__dot{width:34px;height:34px;background:#fff}

  .promo{position:absolute;left:68px;top:208px;width:245px;text-align:center;color:var(--red);font-weight:900}
  .promo__amount{font-size:37px;line-height:1.05}
  .promo__advance{font-size:24px;line-height:1.1}
  .promo__terms{display:flex;align-items:center;gap:4px;color:var(--green);font-size:10.5px;font-weight:900;margin:3px 0 2px}
  .promo__terms::before,.promo__terms::after{content:"";flex:1;height:1.5px;background:var(--green)}
  .promo__free{font-size:29px;line-height:1.1}

  .divider{position:absolute;left:347px;top:79px;width:1px;height:243px;background:var(--ink)}

  .contact{position:absolute;left:381px;top:74px;color:var(--ink)}
  .contact__name{font-size:31px;font-weight:900;color:var(--green);letter-spacing:.3px;line-height:1}
  .contact__title{font-size:19px;color:var(--red);margin-top:4px}
  .contact__list{list-style:none;margin-top:14px;font-size:16.5px}
  .contact__list li{display:flex;align-items:flex-start;gap:11px;line-height:24.5px}
  .contact__list li.gap{margin-bottom:10px}
  .contact__list svg{flex:none;width:13px;height:13px;margin-top:6px;fill:var(--green)}

  .tagline{position:absolute;left:0;right:0;top:238px;text-align:center;color:#fff;font-weight:900}
  .tagline__main{font-size:33px;line-height:1.1}
  .tagline__sub{font-size:26px;line-height:1.1}
</style>
</head>
<body>
<div class="canvas">

  <section class="card card--front">
    <div class="brand"><span class="brand__dot"></span><span>Ledgerline Financial Group</span></div>

    <div class="promo">
      <div class="promo__amount">UP TO $6,000</div>
      <div class="promo__advance">SAME DAY ADVANCE</div>
      <div class="promo__terms">ON APPROVED TAX RETURNS!</div>
      <div class="promo__free">FREE ESTIMATES!</div>
    </div>

    <div class="divider"></div>

    <div class="contact">
      <div class="contact__name">DANIEL REYES</div>
      <div class="contact__title">Founder &amp; CEO</div>
      <ul class="contact__list">
        <li class="gap">
          <svg viewBox="0 0 16 16"><path d="M8 0a5.5 5.5 0 0 0-5.5 5.5C2.5 10 8 16 8 16s5.5-6 5.5-10.5A5.5 5.5 0 0 0 8 0zm0 8a2.5 2.5 0 1 1 0-5 2.5 2.5 0 0 1 0 5z"/></svg>
          <span>Your Address, City<br>State, Country, Zip 1235</span>
        </li>
        <li>
          <svg viewBox="0 0 16 16"><path d="M3.6 1l2.5 3-1.4 1.8a9 9 0 0 0 5.5 5.5L12 9.9l3 2.5-1.6 2.6C7 15 1 9 1 2.6z"/></svg>
          <span>(123) 456-7890</span>
        </li>
        <li>
          <svg viewBox="0 0 16 16"><path d="M4 0h8a1 1 0 0 1 1 1v14a1 1 0 0 1-1 1H4a1 1 0 0 1-1-1V1a1 1 0 0 1 1-1zm1 2v10h6V2zm3 11a1 1 0 1 0 0 2 1 1 0 0 0 0-2z"/></svg>
          <span>(231) 456-7890</span>
        </li>
        <li>
          <svg viewBox="0 0 16 16"><path d="M4 0h8v4H4zM1 5h14v7h-3v-3H4v3H1zm4 5h6v6H5z"/></svg>
          <span>(312) 456-7890</span>
        </li>
        <li>
          <svg viewBox="0 0 16 16"><path d="M0 3h16v10H0zm1.5 1.5v.4L8 9.3l6.5-4.4v-.4zm0 2.2v4.8h13V6.7L8 11z"/></svg>
          <span>office@ledgerline.com</span>
        </li>
        <li>
          <svg viewBox="0 0 16 16"><path d="M8 0a8 8 0 1 0 0 16A8 8 0 0 0 8 0zm0 1.6c.9 0 2 1.7 2.3 4.4H5.7C6 3.3 7.1 1.6 8 1.6zM1.7 7.5h2.5c0 .9.1 1.8.3 2.5H2.1a6.4 6.4 0 0 1-.4-2.5zm9.9 0h2.7c0 .9-.2 1.7-.4 2.5h-2.6c.2-.8.3-1.6.3-2.5zM8 14.4c-.9 0-1.9-1.5-2.3-3.4h4.6c-.4 1.9-1.4 3.4-2.3 3.4z"/></svg>
          <span>www.ledgerline.com</span>
        </li>
      </ul>
    </div>
  </section>

  <section class="card card--back">
    <div class="brand"><span class="brand__dot"></span><span>Ledgerline Financial Group</span></div>
    <div class="tagline">
      <div class="tagline__main">FILE YOUR TAXES HERE</div>
      <div class="tagline__sub">UP TO $6,000 SAME DAY ADVANCE</div>
    </div>
  </section>

</div>
</body>
</html>
```